U.S. based testing, inspection, and certification (TIC) company needs a new PowerPoint template.

We need a new PowerPoint template (deck, slide deck) for our U.S. based company with international capabilities for performing numerous testing, inspection, and certification (TIC) services. Our primary services include calibration, chemical analysis, consulting engineering, environmental simulation, forensic engineering, materials testing, mechanical testing, and nondestructive testing. Industries we serve are aerospace/aviation, automotive, chemical, commercial properties, construction, consumer products, defense, energy storage, healthcare, insurance/legal, life science, manufacturing, oil & gas, power generation, pulp & paper, and telecommunications. https://qirvotest.com/

Guideline hex colors: #29aae2, #0b1f3b, #fb6805 (use orange more subtly)

The final design should communicate:
1. Trust, Integrity, and Independence
2. Technical Expertise and Accuracy
3. Efficiency and Speed
4. Value-Added Partnership

Our current branding reflects a variety of styles, several of which have been included as attachments for reference in this project. While these examples showcase the direction we have taken in the past, we are not limited to them and remain open to exploring fresh, innovative design that is simple, clean, and with plenty of space to add content for each slide. We welcome creative concepts that build on or reimagine our existing identity to better align with our evolving vision.

```html
<!DOCTYPE html>
<html lang="en">
<head>
<meta charset="utf-8">
<title>Qirvo Corporate Presentation Template</title>
<link href="https://fonts.googleapis.com/css2?family=Roboto:wght@400;500;700;900&display=swap" rel="stylesheet">
<style>
:root{
  --navy:#0b1f3b;
  --navy-2:#12305a;
  --blue:#29aae2;
  --blue-deep:#1677d2;
  --orange:#fb6805;
  --ink:#1d2b44;
  --muted:#6b7586;
  --line:#e3e8ef;
  --paper:#ffffff;
  --bg:#eef1f5;
}
*{box-sizing:border-box;margin:0;padding:0}
html,body{width:1200px;height:800px;overflow:hidden;background:var(--bg);font-family:"Roboto",Arial,sans-serif;color:var(--ink)}
.canvas{position:relative;width:1200px;height:800px}
.slide{position:absolute;overflow:hidden;background:var(--paper);box-shadow:0 1px 3px rgba(11,31,59,.12)}
.slide.dark{background:var(--navy);color:#fff}

/* brand */
.brand{position:absolute;display:flex;flex-direction:column;align-items:flex-start}
.brand-name{font-weight:900;font-size:15px;letter-spacing:2px;color:var(--navy);line-height:1}
.brand-sub{font-size:4.5px;color:var(--navy);margin-top:2px;letter-spacing:.2px}
.dark .brand-name,.dark .brand-sub{color:#fff}
.brand.top-right{top:13px;right:18px;align-items:flex-end}

.title{position:absolute;left:22px;top:14px;font-weight:700;font-size:12.5px;color:var(--navy);letter-spacing:.2px}
.title::after{content:"";display:block;width:16px;height:1.5px;background:var(--orange);margin-top:6px}
.small{font-size:5.5px;line-height:1.55;color:var(--muted)}
.label{font-size:5px;font-weight:700;color:var(--navy);text-transform:uppercase;letter-spacing:.2px;text-align:center;line-height:1.3}
.icon{width:16px;height:16px;display:block;margin:0 auto 4px}
.photo{position:absolute}

/* row 1 */
.hero-stripe{position:absolute;background:linear-gradient(160deg,var(--blue) 0%,var(--blue-deep) 100%)}
.hero-head{position:absolute;left:21px;top:80px;font-weight:900;font-size:17.5px;line-height:1.08;letter-spacing:.3px}
.hero-head .accent{color:var(--blue)}
.rule{width:16px;height:1.5px;background:var(--orange)}

.agenda-list{position:absolute;left:26px;top:66px;list-style:none}
.agenda-list li{display:flex;gap:12px;font-size:7px;color:var(--ink);height:14px;align-items:center}
.agenda-list b{color:var(--blue-deep);font-weight:700;width:10px}

/* grids */
.feature-row{position:absolute;left:10px;right:10px;bottom:18px;display:flex}
.feature{flex:1;text-align:center;border-left:1px solid var(--line);padding:0 4px}
.feature:first-child{border-left:0}
.feature .small{text-align:center;margin-top:2px;font-size:5px}

.svc-grid{position:absolute;left:14px;right:14px;top:70px;display:grid;grid-template-columns:repeat(4,1fr);row-gap:22px}
.svc-grid>div{border-left:1px solid var(--line);padding-top:2px}
.svc-grid>div:nth-child(4n+1){border-left:0}

.ind-grid{position:absolute;left:18px;right:18px;top:44px}
.ind-row{display:flex;justify-content:space-between;margin-bottom:10px}
.ind-row>div{width:56px}

/* team */
.stat-band{position:absolute;left:0;right:0;bottom:0;height:48px;background:var(--navy);display:flex;align-items:center;padding:0 16px}
.stat{flex:1;display:flex;gap:6px;align-items:center;border-left:1px solid rgba(255,255,255,.2);padding-left:10px;font-size:5px;line-height:1.3}
.stat:first-child{border-left:0;padding-left:0}
.stat strong{display:block;color:var(--blue);font-size:10px;line-height:1.2}
.stat span{display:block;font-size:4.5px;color:#fff;text-transform:uppercase;line-height:1.3}

/* performance */
.kpi{position:absolute;left:22px;display:flex;gap:10px;align-items:flex-start;font-size:5px;line-height:1.3}
.kpi strong{display:block;color:var(--blue-deep);font-size:8px;line-height:1.2}
.kpi span{font-size:4.5px;color:var(--ink);line-height:1.3;display:block}

/* case */
.case-text{position:absolute;left:20px;top:46px;width:110px}
.case-text h4{font-size:5.5px;color:var(--blue-deep);margin:6px 0 2px;text-transform:uppercase}
.case-text p,.case-text li{font-size:5px;color:var(--muted);line-height:1.55;list-style:none}
.case-text li::before{content:"✓ ";color:var(--blue-deep)}
.case-panel{position:absolute;right:0;top:39px;bottom:0;width:150px;background:var(--navy);padding:16px 8px 0 40px;clip-path:polygon(20% 0,100% 0,100% 100%,0 100%)}
.case-item{display:flex;gap:8px;align-items:flex-start;margin-bottom:14px;color:#fff;font-size:5px;line-height:1.45}
.case-item b{display:block;font-size:5px;text-transform:uppercase}
.case-item span{display:block;font-size:5px;opacity:.85}

/* process */
.steps{position:absolute;left:18px;right:18px;top:46px;display:flex;justify-content:space-between}
.step{width:56px;text-align:center}
.step .ring{width:32px;height:32px;border-radius:50%;border:1.2px solid #c9dff2;margin:0 auto 10px;display:flex;align-items:center;justify-content:center}
.step .label{font-size:6px}
.step .small{font-size:5px;text-align:center}
.tagline{position:absolute;left:0;right:0;bottom:20px;text-align:center;font-size:6.5px;color:var(--blue-deep);font-weight:500}

/* table */
.compare{position:absolute;left:8px;right:8px;top:38px;border-collapse:collapse;font-size:4.3px}
.compare th{height:14px;font-size:5px;text-transform:uppercase}
.compare th.us{background:var(--blue-deep);color:#fff}
.compare th.them{background:#e9edf2;color:var(--ink)}
.compare td{height:15.8px;border-bottom:1px solid var(--line);text-align:center;color:var(--muted)}
.compare td.crit{text-align:left;font-weight:700;color:var(--navy);text-transform:uppercase}
.compare td.us{background:#f6f9fc}

/* journey */
.timeline{position:absolute;left:14px;right:14px;top:56px;display:flex;justify-content:space-between}
.timeline::before{content:"";position:absolute;left:20px;right:20px;top:8px;height:1px;background:#c9d4e2}
.milestone{position:relative;width:52px;text-align:center}
.milestone .dot{width:16px;height:16px;border-radius:50%;background:var(--navy);margin:0 auto 8px;border:2px solid #c9dff2}
.milestone b{display:block;font-size:6px;color:var(--navy);margin-bottom:3px}
.milestone p{font-size:4.5px;color:var(--muted);line-height:1.5}
</style>
</head>
<body>
<div class="canvas">

<!-- ROW 1 -->
<section class="slide dark" style="left:9px;top:7px;width:381px;height:211px">
  <div class="photo" role="img" aria-label="Earth seen from orbit at night" style="left:180px;top:0;width:201px;height:211px;background:radial-gradient(circle at 85% 70%,#3b6ea8 0%,#1a3f70 40%,var(--navy) 75%);clip-path:polygon(40% 0,100% 0,100% 100%,0 100%)"></div>
  <div class="hero-stripe" style="left:230px;top:0;width:60px;height:211px;clip-path:polygon(70% 0,100% 0,30% 100%,0 100%);opacity:.85"></div>
  <div class="brand" style="left:21px;top:26px"><span class="brand-name" style="font-size:22px">QIRVO</span><span class="brand-sub" style="font-size:6px">Qirvo Testing Services</span></div>
  <h1 class="hero-head">TESTED.<br><span class="accent">TRUSTED.</span><br>DEPENDABLE.</h1>
  <p style="position:absolute;left:21px;top:145px;font-size:7.5px;line-height:1.4">Global Testing, Inspection<br>&amp; Certification Solutions</p>
  <div class="rule" style="position:absolute;left:21px;top:174px"></div>
  <p style="position:absolute;left:21px;top:183px;font-size:5.5px">Corporate Presentation</p>
</section>

<section class="slide dark" style="left:402px;top:7px;width:376px;height:211px">
  <div class="photo" role="img" aria-label="Faint engineering drawing of a turbine" style="left:150px;top:0;width:226px;height:211px;background:radial-gradient(circle at 55% 45%,#1c3b66 0%,var(--navy) 70%);opacity:.9"></div>
  <div class="hero-stripe" style="left:276px;top:90px;width:100px;height:121px;clip-path:polygon(100% 0,100% 100%,0 100%)"></div>
  <div class="brand top-right"><span class="brand-name">QIRVO</span><span class="brand-sub">Qirvo Testing Services</span></div>
  <p style="position:absolute;left:24px;top:55px;font-size:7px;color:var(--orange);font-weight:500">SECTION 01</p>
  <h2 style="position:absolute;left:24px;top:70px;font-weight:900;font-size:22px;line-height:1.05">ABOUT<br>QIRVO</h2>
  <div class="rule" style="position:absolute;left:24px;top:130px"></div>
  <p style="position:absolute;left:24px;top:140px;font-size:7.5px;line-height:1.5">Independent. Accurate.<br>Trusted Worldwide.</p>
</section>

<section class="slide" style="left:788px;top:7px;width:400px;height:211px">
  <div class="photo" role="img" aria-label="Scientist working at a laboratory microscope" style="left:200px;top:60px;width:200px;height:151px;background:linear-gradient(135deg,#dfe8f2 0%,#a9bfd6 55%,#5a7fa6 100%);clip-path:polygon(30% 0,100% 0,100% 100%,0 100%)"></div>
  <div class="brand top-right"><span class="brand-name">QIRVO</span><span class="brand-sub">Qirvo Testing Services</span></div>
  <div class="title" style="left:26px;top:24px;font-size:14px">AGENDA</div>
  <ol class="agenda-list">
    <li><b>01</b>About Qirvo</li><li><b>02</b>Our Services</li><li><b>03</b>Industries We Serve</li>
    <li><b>04</b>Technical Excellence</li><li><b>05</b>Our Process</li><li><b>06</b>Case Studies</li>
    <li><b>07</b>Our Team</li><li><b>08</b>Data &amp; Performance</li><li><b>09</b>Looking Ahead</li>
  </ol>
</section>

<!-- ROW 2 -->
<section class="slide" style="left:9px;top:227px;width:381px;height:189px">
  <div class="photo" role="img" aria-label="Dotted world map" style="left:180px;top:20px;width:190px;height:95px;background:radial-gradient(ellipse at 50% 50%,#e6ebf1 0%,#f4f6f9 60%,#fff 100%)"></div>
  <div class="brand top-right"><span class="brand-name">QIRVO</span><span class="brand-sub">Qirvo Testing Services</span></div>
  <div class="title">ABOUT QIRVO</div>
  <p class="small" style="position:absolute;left:22px;top:45px;width:140px">Qirvo Testing Services is a global independent testing, inspection, and certification company delivering technical solutions that ensure safety, quality, and performance.</p>
  <div class="feature-row">
    <div class="feature"><svg class="icon" viewBox="0 0 16 16" fill="none" stroke="#1677d2" stroke-width="1.2"><path d="M8 1.5l5 2v4c0 3.5-2.3 5.8-5 7-2.7-1.2-5-3.5-5-7v-4z"/><path d="M5.5 8l2 2 3-3.5"/></svg><div class="label">Independent</div><p class="small">Unbiased and<br>objective results</p></div>
    <div class="feature"><svg class="icon" viewBox="0 0 16 16" fill="none" stroke="#1677d2" stroke-width="1.2"><circle cx="8" cy="6" r="3"/><path d="M3 14c1-3 3-4 5-4s4 1 5 4"/></svg><div class="label">Expert</div><p class="small">Decades of technical<br>knowledge</p></div>
    <div class="feature"><svg class="icon" viewBox="0 0 16 16" fill="none" stroke="#1677d2" stroke-width="1.2"><circle cx="8" cy="8" r="6"/><path d="M2 8h12M8 2c2 2 2 10 0 12M8 2c-2 2-2 10 0 12"/></svg><div class="label">Global</div><p class="small">International reach<br>local expertise</p></div>
    <div class="feature"><svg class="icon" viewBox="0 0 16 16" fill="none" stroke="#1677d2" stroke-width="1.2"><path d="M8 1.5l5 2v4c0 3.5-2.3 5.8-5 7-2.7-1.2-5-3.5-5-7v-4z"/><path d="M5.5 8l2 2 3-3.5"/></svg><div class="label">Trusted</div><p class="small">Committed to integrity,<br>accuracy, and safety</p></div>
  </div>
</section>

<section class="slide" style="left:402px;top:227px;width:376px;height:189px">
  <div class="brand top-right"><span class="brand-name">QIRVO</span><span class="brand-sub">Qirvo Testing Services</span></div>
  <div class="title">OUR SERVICES</div>
  <p class="small" style="position:absolute;left:22px;top:40px">Comprehensive Testing, Inspection<br>&amp; Certification Solutions</p>
  <div class="svc-grid">
    <div><svg class="icon" viewBox="0 0 16 16" fill="none" stroke="#1677d2" stroke-width="1.2"><circle cx="8" cy="8" r="6"/><path d="M8 8l3-3"/></svg><div class="label">Calibration</div></div>
    <div><svg class="icon" viewBox="0 0 16 16" fill="none" stroke="#1677d2" stroke-width="1.2"><path d="M6 2h4M7 2v5l-4 7h10l-4-7V2"/></svg><div class="label">Chemical Analysis</div></div>
    <div><svg class="icon" viewBox="0 0 16 16" fill="none" stroke="#1677d2" stroke-width="1.2"><circle cx="6" cy="5" r="2.5"/><circle cx="11" cy="6" r="2"/><path d="M2 14c0-3 2-5 4-5s4 2 4 5M10 10c2 0 4 1 4 4"/></svg><div class="label">Consulting<br>Engineering</div></div>
    <div><svg class="icon" viewBox="0 0 16 16" fill="none" stroke="#1677d2" stroke-width="1.2"><circle cx="8" cy="8" r="3"/><path d="M8 1v2M8 13v2M1 8h2M13 8h2M3 3l1.5 1.5M11.5 11.5L13 13M13 3l-1.5 1.5M3 13l1.5-1.5"/></svg><div class="label">Environmental<br>Simulation</div></div>
    <div><svg class="icon" viewBox="0 0 16 16" fill="none" stroke="#1677d2" stroke-width="1.2"><circle cx="7" cy="7" r="4.5"/><path d="M10.5 10.5L14 14"/></svg><div class="label">Forensic<br>Engineering</div></div>
    <div><svg class="icon" viewBox="0 0 16 16" fill="none" stroke="#1677d2" stroke-width="1.2"><rect x="3" y="2" width="10" height="12" rx="1"/><path d="M5 11l6-6"/></svg><div class="label">Materials<br>Testing</div></div>
    <div><svg class="icon" viewBox="0 0 16 16" fill="none" stroke="#1677d2" stroke-width="1.2"><circle cx="8" cy="8" r="2.5"/><circle cx="8" cy="8" r="5.5" stroke-dasharray="2 1.5"/></svg><div class="label">Mechanical<br>Testing</div></div>
    <div><svg class="icon" viewBox="0 0 16 16" fill="none" stroke="#1677d2" stroke-width="1.2"><circle cx="8" cy="8" r="6"/><path d="M4 9l2-3 2 4 2-3 2 2"/></svg><div class="label">Nondestructive<br>Testing</div></div>
  </div>
</section>

<section class="slide" style="left:788px;top:227px;width:400px;height:189px">
  <div class="brand top-right"><span class="brand-name">QIRVO</span><span class="brand-sub">Qirvo Testing Services</span></div>
  <div class="title">INDUSTRIES WE SERVE</div>
  <div class="ind-grid">
    <div class="ind-row" style="padding:0 40px">
      <div><svg class="icon" viewBox="0 0 16 16" fill="none" stroke="#1677d2" stroke-width="1.2"><path d="M2 9l12-6-4 10-2-4z"/></svg><div class="label">Aerospace /<br>Aviation</div></div>
      <div><svg class="icon" viewBox="0 0 16 16" fill="none" stroke="#1677d2" stroke-width="1.2"><path d="M2 11V8l2-3h8l2 3v3z"/><circle cx="5" cy="11.5" r="1.3"/><circle cx="11" cy="11.5" r="1.3"/></svg><div class="label">Automotive</div></div>
      <div><svg class="icon" viewBox="0 0 16 16" fill="none" stroke="#1677d2" stroke-width="1.2"><path d="M6 2h4M7 2v5l-4 7h10l-4-7V2"/></svg><div class="label">Chemical</div></div>
      <div><svg class="icon" viewBox="0 0 16 16" fill="none" stroke="#1677d2" stroke-width="1.2"><rect x="4" y="2" width="8" height="12"/><path d="M6 5h1M9 5h1M6 8h1M9 8h1M6 11h1M9 11h1"/></svg><div class="label">Commercial<br>Properties</div></div>
      <div><svg class="icon" viewBox="0 0 16 16" fill="none" stroke="#1677d2" stroke-width="1.2"><path d="M2 14h12M4 14V6l4-4 4 4v8"/></svg><div class="label">Construction</div></div>
    </div>
    <div class="ind-row" style="padding:0 40px">
      <div><svg class="icon" viewBox="0 0 16 16" fill="none" stroke="#1677d2" stroke-width="1.2"><path d="M4 7h8l-1 7H5zM6 7V4a2 2 0 014 0v3"/></svg><div class="label">Consumer<br>Products</div></div>
      <div><svg class="icon" viewBox="0 0 16 16" fill="none" stroke="#1677d2" stroke-width="1.2"><path d="M8 1.5l1.9 4 4.3.5-3.2 3 .9 4.3L8 11.2 4.1 13.3 5 9 1.8 6l4.3-.5z"/></svg><div class="label">Defense</div></div>
      <div><svg class="icon" viewBox="0 0 16 16" fill="none" stroke="#1677d2" stroke-width="1.2"><rect x="4" y="3" width="8" height="11" rx="1"/><path d="M7 1.5h2M8.5 6L7 9h2l-1.5 3"/></svg><div class="label">Energy<br>Storage</div></div>
      <div><svg class="icon" viewBox="0 0 16 16" fill="none" stroke="#1677d2" stroke-width="1.2"><path d="M8 14S2 10 2 6a3 3 0 016-1 3 3 0 016 1c0 4-6 8-6 8z"/></svg><div class="label">Healthcare</div></div>
      <div><svg class="icon" viewBox="0 0 16 16" fill="none" stroke="#1677d2" stroke-width="1.2"><path d="M8 2v12M4 14h8M3 5h10M3 5l-1.5 4h3zM13 5l-1.5 4h3z"/></svg><div class="label">Insurance /<br>Legal</div></div>
    </div>
    <div class="ind-row">
      <div><svg class="icon" viewBox="0 0 16 16" fill="none" stroke="#1677d2" stroke-width="1.2"><path d="M5 2c4 3 2 9 6 12M11 2C7 5 9 11 5 14M6 5h4M6 11h4"/></svg><div class="label">Life Science</div></div>
      <div><svg class="icon" viewBox="0 0 16 16" fill="none" stroke="#1677d2" stroke-width="1.2"><path d="M2 14V8l4 2V8l4 2V4h4v10z"/></svg><div class="label">Manufacturing</div></div>
      <div><svg class="icon" viewBox="0 0 16 16" fill="none" stroke="#1677d2" stroke-width="1.2"><path d="M8 2s5 6 5 9a5 5 0 01-10 0c0-3 5-9 5-9z"/></svg><div class="label">Oil &amp; Gas</div></div>
      <div><svg class="icon" viewBox="0 0 16 16" fill="none" stroke="#1677d2" stroke-width="1.2"><circle cx="8" cy="8" r="6"/><path d="M9 3L6 9h3l-1 4"/></svg><div class="label">Power<br>Generation</div></div>
      <div><svg class="icon" viewBox="0 0 16 16" fill="none" stroke="#1677d2" stroke-width="1.2"><path d="M2 14V7h3v7M6 14V4h4v10M11 14V9h3v5"/></svg><div class="label">Pulp &amp; Paper</div></div>
      <div><svg class="icon" viewBox="0 0 16 16" fill="none" stroke="#1677d2" stroke-width="1.2"><path d="M8 7v7M5 14h6M4 4a5 5 0 008 0M6 5a2.5 2.5 0 004 0"/></svg><div class="label">Telecommunications</div></div>
    </div>
  </div>
</section>

<!-- ROW 3 -->
<section class="slide" style="left:9px;top:426px;width:381px;height:184px">
  <div class="photo" role="img" aria-label="Three team members: lab scientist, technician and engineer" style="left:88px;top:42px;width:293px;height:94px;background:linear-gradient(90deg,#c7d4e3 0%,#8fa7c2 35%,#2f4f7a 55%,#b9c8d9 75%,#dde5ee 100%);clip-path:polygon(12% 0,100% 0,100% 100%,0 100%)"></div>
  <div class="brand top-right"><span class="brand-name">QIRVO</span><span class="brand-sub">Qirvo Testing Services</span></div>
  <div class="title">OUR TEAM</div>
  <p class="small" style="position:absolute;left:22px;top:44px;width:66px;font-size:5px">Our people are our greatest strength.<br><br>Engineers, scientists, technicians, and inspectors working together to deliver technical excellence.</p>
  <div class="stat-band">
    <div class="stat"><svg width="12" height="12" viewBox="0 0 16 16" fill="none" stroke="#29aae2" stroke-width="1.2"><circle cx="8" cy="5" r="3"/><path d="M2 15c1-4 3-5 6-5s5 1 6 5"/></svg><div><strong>2,500+</strong><span>Professionals</span></div></div>
    <div class="stat"><svg width="12" height="12" viewBox="0 0 16 16" fill="none" stroke="#29aae2" stroke-width="1.2"><circle cx="8" cy="8" r="6"/><path d="M6 5v6M10 5v6"/></svg><div><strong>100+</strong><span>Laboratories<br>&amp; Facilities</span></div></div>
    <div class="stat"><svg width="12" height="12" viewBox="0 0 16 16" fill="none" stroke="#fff" stroke-width="1.2"><circle cx="8" cy="8" r="6"/><path d="M2 8h12M8 2c2 2 2 10 0 12M8 2c-2 2-2 10 0 12"/></svg><div><strong>50+</strong><span>Countries<br>Served</span></div></div>
    <div class="stat"><svg width="12" height="12" viewBox="0 0 16 16" fill="none" stroke="#29aae2" stroke-width="1.2"><path d="M8 1.5l5 2v4c0 3.5-2.3 5.8-5 7-2.7-1.2-5-3.5-5-7v-4z"/></svg><div><strong>60+</strong><span>Years of<br>Experience</span></div></div>
  </div>
</section>

<section class="slide" style="left:402px;top:426px;width:376px;height:184px">
  <div class="brand top-right"><span class="brand-name">QIRVO</span><span class="brand-sub">Qirvo Testing Services</span></div>
  <div class="title">PERFORMANCE AT A GLANCE</div>
  <div class="kpi" style="top:46px"><svg width="14" height="14" viewBox="0 0 16 16" fill="none" stroke="#1677d2" stroke-width="1.2"><circle cx="8" cy="8" r="5"/><circle cx="8" cy="8" r="2"/></svg><div><strong>20M+</strong><span>Tests Performed<br>Annually</span></div></div>
  <div class="kpi" style="top:77px"><svg width="14" height="14" viewBox="0 0 16 16" fill="none" stroke="#1677d2" stroke-width="1.2"><circle cx="8" cy="8" r="6"/><path d="M8 4v4l3 2"/></svg><div><strong>98.7%</strong><span>On-Time Delivery</span></div></div>
  <div class="kpi" style="top:104px"><svg width="14" height="14" viewBox="0 0 16 16" fill="none" stroke="#1677d2" stroke-width="1.2"><path d="M2 8h3v6H2zM5 8l3-5 1 1-1 4h5l-1 6H5"/></svg><div><strong>99.5%</strong><span>Customer Satisfaction</span></div></div>
  <div class="kpi" style="top:133px"><svg width="14" height="14" viewBox="0 0 16 16" fill="none" stroke="#1677d2" stroke-width="1.2"><circle cx="8" cy="8" r="6"/><path d="M5.5 8l2 2 3-3.5"/></svg><div><strong>0</strong><span>Compromises on<br>Quality &amp; Integrity</span></div></div>
  <svg style="position:absolute;left:112px;top:44px" width="150" height="130" viewBox="0 0 150 130" font-family="Roboto,Arial,sans-serif">
    <text x="22" y="8" font-size="5" font-weight="700" fill="#0b1f3b">TESTS PERFORMED (ANNUALLY)</text>
    <g font-size="4" fill="#6b7586" text-anchor="end">
      <text x="14" y="25">25M</text><text x="14" y="40">20M</text><text x="14" y="54">15M</text><text x="14" y="69">10M</text><text x="14" y="83">5M</text><text x="14" y="97">0</text>
    </g>
    <line x1="18" y1="96" x2="112" y2="96" stroke="#c9d4e2" stroke-width=".6"/>
    <g fill="#1677d2">
      <rect x="24" y="66" width="9" height="30"/><rect x="42" y="57" width="9" height="39"/><rect x="60" y="51" width="9" height="45"/><rect x="78" y="45" width="9" height="51"/><rect x="96" y="37" width="9" height="59"/>
    </g>
    <g font-size="4" fill="#6b7586" text-anchor="middle">
      <text x="28.5" y="104">2021</text><text x="46.5" y="104">2022</text><text x="64.5" y="104">2023</text><text x="82.5" y="104">2024</text><text x="100.5" y="104">2025</text>
    </g>
  </svg>
  <svg style="position:absolute;left:236px;top:44px" width="130" height="100" viewBox="0 0 130 100" font-family="Roboto,Arial,sans-serif">
    <text x="18" y="8" font-size="5" font-weight="700" fill="#0b1f3b">SERVICE MIX</text>
    <g transform="translate(34,55)" fill="none" stroke-width="11">
      <circle r="24" stroke="#0b1f3b" stroke-dasharray="60 151"/>
      <circle r="24" stroke="#1677d2" stroke-dasharray="40 151" stroke-dashoffset="-60"/>
      <circle r="24" stroke="#29aae2" stroke-dasharray="25 151" stroke-dashoffset="-100"/>
      <circle r="24" stroke="#8fc6ea" stroke-dasharray="14 151" stroke-dashoffset="-125"/>
      <circle r="24" stroke="#cfd9e4" stroke-dasharray="12 151" stroke-dashoffset="-139"/>
    </g>
    <g font-size="4.3" fill="#6b7586">
      <circle cx="68" cy="34" r="1.6" fill="#0b1f3b"/><text x="73" y="35.5">Mechanical Testing</text>
      <circle cx="68" cy="45" r="1.6" fill="#1677d2"/><text x="73" y="46.5">Chemical Analysis</text>
      <circle cx="68" cy="56" r="1.6" fill="#29aae2"/><text x="73" y="57.5">NDT</text>
      <circle cx="68" cy="67" r="1.6" fill="#8fc6ea"/><text x="73" y="68.5">Calibration</text>
      <circle cx="68" cy="78" r="1.6" fill="#cfd9e4"/><text x="73" y="79.5">Other Services</text>
    </g>
  </svg>
</section>

<section class="slide" style="left:788px;top:426px;width:400px;height:184px">
  <div class="photo" role="img" aria-label="Close-up of a jet engine turbine" style="left:134px;top:39px;width:150px;height:145px;background:radial-gradient(circle at 40% 50%,#0e1a2c 0%,#3c4c62 45%,#a9b6c6 80%,#dfe6ee 100%);clip-path:polygon(0 0,100% 0,100% 100%,12% 100%)"></div>
  <div class="brand top-right"><span class="brand-name">QIRVO</span><span class="brand-sub">Qirvo Testing Services</span></div>
  <div class="title" style="left:20px">CASE STUDY</div>
  <div class="case-text">
    <h4>Client Challenge</h4><p>Complex material failure impacting product performance and safety.</p>
    <h4>Qirvo Solution</h4><p>Comprehensive failure analysis using advanced testing, inspection, and engineering expertise.</p>
    <h4>Results</h4>
    <ul><li>Root cause identified</li><li>Product performance improved</li><li>Costly downtime minimized</li></ul>
  </div>
  <div class="case-panel">
    <div class="case-item"><svg width="11" height="11" viewBox="0 0 16 16" fill="none" stroke="#29aae2" stroke-width="1.3"><circle cx="8" cy="5" r="3"/><path d="M2 15c1-4 3-5 6-5s5 1 6 5"/></svg><div><b>Industry</b><span>Aerospace</span></div></div>
    <div class="case-item"><svg width="11" height="11" viewBox="0 0 16 16" fill="none" stroke="#29aae2" stroke-width="1.3"><circle cx="6" cy="5" r="2.5"/><path d="M2 14c0-3 2-5 4-5s4 2 4 5"/></svg><div><b>Service</b><span>Failure Analysis</span></div></div>
    <div class="case-item"><svg width="11" height="11" viewBox="0 0 16 16" fill="none" stroke="#29aae2" stroke-width="1.3"><circle cx="8" cy="8" r="6"/><path d="M8 4v4l3 2"/></svg><div><b>Duration</b><span>4 Weeks</span></div></div>
    <div class="case-item"><svg width="11" height="11" viewBox="0 0 16 16" fill="none" stroke="#29aae2" stroke-width="1.3"><circle cx="8" cy="8" r="6"/><path d="M5.5 8l2 2 3-3.5"/></svg><div><b>Impact</b><span>Enhanced Safety<br>&amp; Reliability</span></div></div>
  </div>
</section>

<!-- ROW 4 -->
<section class="slide" style="left:9px;top:618px;width:381px;height:173px">
  <div class="brand top-right"><span class="brand-name">QIRVO</span><span class="brand-sub">Qirvo Testing Services</span></div>
  <div class="title">OUR PROCESS</div>
  <div class="steps">
    <div class="step"><div class="ring"><svg width="13" height="13" viewBox="0 0 16 16" fill="none" stroke="#1677d2" stroke-width="1.2"><circle cx="8" cy="5" r="3"/><path d="M2 15c1-4 3-5 6-5s5 1 6 5"/></svg></div><div class="label">Understand</div><p class="small">Your requirements<br>and objectives</p></div>
    <div class="step"><div class="ring"><svg width="13" height="13" viewBox="0 0 16 16" fill="none" stroke="#1677d2" stroke-width="1.2"><rect x="3" y="2" width="10" height="12" rx="1"/><path d="M5 6h6M5 9h6M5 12h3"/></svg></div><div class="label">Plan</div><p class="small">Develop testing<br>and inspection plan</p></div>
    <div class="step"><div class="ring"><svg width="13" height="13" viewBox="0 0 16 16" fill="none" stroke="#1677d2" stroke-width="1.2"><circle cx="8" cy="8" r="2.5"/><circle cx="8" cy="8" r="5.5" stroke-dasharray="2 1.5"/></svg></div><div class="label">Execute</div><p class="small">Perform testing<br>with precision</p></div>
    <div class="step"><div class="ring"><svg width="13" height="13" viewBox="0 0 16 16" fill="none" stroke="#1677d2" stroke-width="1.2"><path d="M2 14h12M4 12V8M8 12V4M12 12V7"/></svg></div><div class="label">Analyze</div><p class="small">Evaluate and<br>interpret results</p></div>
    <div class="step"><div class="ring"><svg width="13" height="13" viewBox="0 0 16 16" fill="none" stroke="#1677d2" stroke-width="1.2"><circle cx="8" cy="8" r="6"/><path d="M8 4v7M5 8l3 3 3-3"/></svg></div><div class="label">Deliver</div><p class="small">Provide clear<br>reports &amp; insights</p></div>
  </div>
  <svg style="position:absolute;left:0;top:62px" width="381" height="8" viewBox="0 0 381 8" fill="none" stroke="#1677d2" stroke-width=".8">
    <path d="M75 4h12M84 1.5L87 4l-3 2.5M143 4h12M152 1.5L155 4l-3 2.5M211 4h12M220 1.5L223 4l-3 2.5M279 4h12M288 1.5L291 4l-3 2.5"/>
  </svg>
  <p class="tagline"><span style="color:var(--orange)">—</span> Quality. Integrity. Independence. Every Step of the Way.</p>
</section>

<section class="slide" style="left:401px;top:618px;width:193px;height:173px">
  <div class="brand top-right" style="right:12px"><span class="brand-name" style="font-size:12px">QIRVO</span><span class="brand-sub" style="font-size:3.5px">Qirvo Testing Services</span></div>
  <div class="title" style="left:12px;font-size:9px">WHY QIRVO</div>
  <table class="compare">
    <thead><tr><th></th><th class="us">Qirvo</th><th class="them">Others</th></tr></thead>
    <tbody>
      <tr><td class="crit">Independence</td><td class="us">100% Independent</td><td>May have conflicts</td></tr>
      <tr><td class="crit">Technical Expertise</td><td class="us">Highly Specialized</td><td>Limited Resources</td></tr>
      <tr><td class="crit">Global Network</td><td class="us">Extensive</td><td>Limited Reach</td></tr>
      <tr><td class="crit">Turnaround Time</td><td class="us">Fast &amp; Reliable</td><td>Variable</td></tr>
      <tr><td class="crit">Quality Standards</td><td class="us">Industry Leading</td><td>Standard</td></tr>
      <tr><td class="crit">Customer Focus</td><td class="us">Partnership Approach</td><td>Transactional</td></tr>
    </tbody>
  </table>
</section>

<section class="slide" style="left:603px;top:618px;width:289px;height:173px">
  <div class="brand top-right" style="right:16px"><span class="brand-name" style="font-size:12px">QIRVO</span><span class="brand-sub" style="font-size:3.5px">Qirvo Testing Services</span></div>
  <div class="title" style="left:19px;font-size:10.5px">OUR JOURNEY</div>
  <div class="timeline">
    <div class="milestone"><div class="dot"></div><b>1967</b><p>Founded with a commitment to technical excellence</p></div>
    <div class="milestone"><div class="dot"></div><b>1990s</b><p>Expanded laboratory capabilities &amp; global reach</p></div>
    <div class="milestone"><div class="dot"></div><b>2000s</b><p>Advanced technology &amp; service diversification</p></div>
    <div class="milestone"><div class="dot"></div><b>2010s</b><p>Strengthened global presence &amp; innovation</p></div>
    <div class="milestone"><div class="dot"></div><b>2020+</b><p>Continuing to lead the future of TIC services</p></div>
  </div>
  <p class="tagline" style="bottom:24px">Built on Experience. Driven by Innovation. Focused on the Future.</p>
</section>

<section class="slide dark" style="left:900px;top:618px;width:288px;height:173px">
  <div class="photo" role="img" aria-label="Faint blueprint of a turbine" style="left:150px;top:30px;width:138px;height:143px;background:radial-gradient(circle at 50% 50%,#1d3d68 0%,var(--navy) 70%)"></div>
  <div class="hero-stripe" style="left:198px;top:70px;width:90px;height:103px;clip-path:polygon(100% 0,100% 100%,0 100%)"></div>
  <div class="brand top-right"><span class="brand-name">QIRVO</span><span class="brand-sub">Qirvo Testing Services</span></div>
  <h2 style="position:absolute;left:22px;top:49px;font-weight:900;font-size:18px">THANK <span style="color:var(--blue)">YOU</span></h2>
  <div class="rule" style="position:absolute;left:22px;top:78px"></div>
  <p style="position:absolute;left:22px;top:88px;font-size:7px;line-height:1.5">Your Partner in Quality,<br>Safety &amp; Performance</p>
  <p style="position:absolute;left:22px;top:150px;font-size:5px">www.qirvotest.com</p>
</section>

</div>
</body>
</html>
```